Providing Back Office Solutions to Financial Advisors and Attorney Needs a Business Card Design

Need a Business Card Design that speaks to Financial Advisor and Attorneys. Some of the word that come to mind is Clean/Simple & Futuristic.

Industry/Entity Type

Business

```html
<!DOCTYPE html>
<html lang="en">
<head>
<meta charset="utf-8">
<title>Corvane Back Office Solutions – Business Card</title>
<link rel="stylesheet" href="https://fonts.googleapis.com/css2?family=Lato:wght@400;700&display=swap">
<style>
  :root {
    --backdrop: #ece3d6;
    --card-white: #ffffff;
    --ink-blue: #0f5fa6;
    --ink-dark: #2b2b2b;
    --rule-grey: #b9bcc2;
    --blue-top: #0a5a94;
    --blue-bottom: #0a7dc2;
    --on-blue: #ffffff;
  }
  * { margin: 0; padding: 0; box-sizing: border-box; }
  html, body {
    width: 1200px; height: 900px; overflow: hidden;
    background: var(--backdrop);
    font-family: "Lato", sans-serif;
  }
  .canvas { position: relative; width: 1200px; height: 900px; }

  .card {
    position: absolute; top: 275px; width: 479px; height: 295px;
    box-shadow: 0 3px 8px rgba(0,0,0,0.25);
  }
  .card--front {
    left: 116px; background: var(--card-white);
    border-radius: 6px 48px 6px 48px;
  }
  .card--back {
    left: 622px;
    background: linear-gradient(180deg, var(--blue-top), var(--blue-bottom));
    border-radius: 48px 6px 48px 6px;
  }

  .brand { position: absolute; display: flex; align-items: center; }
  .brand__mark { flex: none; }
  .brand__divider { width: 2px; align-self: stretch; margin: 0 8px; }
  .brand__text { display: flex; flex-direction: column; }
  .brand__name { font-weight: 400; letter-spacing: 2px; line-height: 1; }
  .brand__tagline { font-weight: 400; line-height: 1; }

  .card--front .brand { left: 192px; top: 50px; height: 70px; color: var(--ink-blue); }
  .card--front .brand__mark { width: 46px; height: 46px; background: var(--ink-blue); }
  .card--front .brand__divider { background: var(--ink-blue); }
  .card--front .brand__name { font-size: 40px; }
  .card--front .brand__tagline { font-size: 14px; margin-top: 10px; }

  .card--back .brand { left: 98px; top: 93px; height: 108px; color: var(--on-blue); }
  .card--back .brand__mark { width: 66px; height: 66px; background: var(--on-blue); }
  .card--back .brand__divider { background: var(--on-blue); margin: 0 14px; }
  .card--back .brand__name { font-size: 48px; }
  .card--back .brand__tagline { font-size: 17px; margin-top: 12px; }

  .holder { position: absolute; left: 29px; top: 165px; right: 28px; }
  .holder__name { font-size: 18px; color: var(--ink-blue); font-weight: 400; letter-spacing: 0.5px; }
  .holder__role { display: flex; align-items: center; font-size: 13px; color: var(--ink-dark); margin-top: 2px; }
  .holder__role::after { content: ""; flex: 1; height: 1px; background: var(--rule-grey); margin-left: 8px; }

  .contacts { position: absolute; left: 29px; top: 216px; list-style: none; font-size: 13px; color: var(--ink-dark); }
  .contacts li { display: flex; align-items: center; height: 17.5px; }
  .contacts svg { width: 10px; height: 10px; margin-right: 6px; fill: var(--ink-blue); }

  .address { position: absolute; right: 37px; top: 234px; text-align: right; font-size: 13px; color: var(--ink-dark); font-style: normal; line-height: 17.5px; }
</style>
</head>
<body>
<main class="canvas">
  <section class="card card--front" aria-label="Card front">
    <div class="brand">
      <span class="brand__mark"></span>
      <span class="brand__divider"></span>
      <div class="brand__text">
        <span class="brand__name">CORVANE</span>
        <span class="brand__tagline">BACK OFFICE SOLUTIONS</span>
      </div>
    </div>

    <div class="holder">
      <h1 class="holder__name">MARCUS HALE</h1>
      <p class="holder__role">Managing Director</p>
    </div>

    <ul class="contacts">
      <li><svg viewBox="0 0 10 10" aria-hidden="true"><path d="M1 3.5C1 2 2.5 1.5 5 1.5S9 2 9 3.5L7.5 4.2 7 3.2H3L2.5 4.2Z"/><rect x="2" y="5" width="6" height="4" rx="0.8"/></svg>044-555 010 234</li>
      <li><svg viewBox="0 0 10 10" aria-hidden="true"><path d="M1 2.5h8v5H1z M1 2.5l4 3 4-3" stroke="#fff" stroke-width="0.6"/></svg>info@corvane.com</li>
      <li><svg viewBox="0 0 10 10" aria-hidden="true"><circle cx="5" cy="5" r="4.3"/><path d="M1 5h8M5 0.8c-2 2.5-2 5.9 0 8.4M5 0.8c2 2.5 2 5.9 0 8.4" stroke="#fff" stroke-width="0.6" fill="none"/></svg>www.corvane.com</li>
    </ul>

    <address class="address">1234, Address GoesHere<br>Country, 12345</address>
  </section>

  <section class="card card--back" aria-label="Card back">
    <div class="brand">
      <span class="brand__mark"></span>
      <span class="brand__divider"></span>
      <div class="brand__text">
        <span class="brand__name">CORVANE</span>
        <span class="brand__tagline">BACK OFFICE SOLUTIONS</span>
      </div>
    </div>
  </section>
</main>
</body>
</html>
```